Whitcombe MD Crest Primary Care Business Card

Need a business card for a medical clinic targeting VIP patients. Should portray an upscale feeling. Simple, clean design. Logo and colors need to be incorporated into card. Clinic colors are gray/ silver, blues, white same as logo.
Clinic is a cash only VIP service clinic targeting higher income patients.
Tagline: "Where each patient is treated as our only patient"

Target Market(s)

VIP, upscale

Industry/Entity Type

Medical

Contact Information for Business Card

Would like to use for cards with raised print or metallic highlight.

Requirements
Must have
• Incorporate logo, Use colors in logo
Nice to have
• Metallic detail
Should not have
• too much details or colors, other stock photos or designs

```html
<!DOCTYPE html>
<html lang="en">
<head>
<meta charset="utf-8">
<title>Whitcombe MD Crest Primary Care Business Card</title>
<link href="https://fonts.googleapis.com/css2?family=Cinzel:wght@400;500&family=Roboto:wght@400;500&display=swap" rel="stylesheet">
<style>
  :root {
    --backdrop: #2a2a2b;
    --card-light: #f3f3f3;
    --card-dark: #19191a;
    --name-blue: #3e5272;
    --title-gray: #9ca2aa;
    --body-gray: #3f3f42;
    --silver: #c9c9cc;
    --white: #f5f5f5;
  }
  * { margin: 0; padding: 0; box-sizing: border-box; }
  html, body { width: 1200px; height: 960px; overflow: hidden; }
  body { background: var(--backdrop); position: relative; font-family: "Roboto", Arial, sans-serif; }

  .card { position: absolute; width: 600px; height: 343px; }
  .card-front { left: 314px; top: 113px; background: var(--card-light); }
  .card-back { left: 312px; top: 473px; background: var(--card-dark); }

  .identity { position: absolute; left: 80px; top: 129px; }
  .person-name { font-family: "Cinzel", Georgia, serif; font-weight: 500; font-size: 22px; color: var(--name-blue); line-height: 1.1; letter-spacing: 0.3px; }
  .person-title { font-family: "Cinzel", Georgia, serif; font-size: 17px; color: var(--title-gray); line-height: 1.1; margin-bottom: 4px; }
  .address { font-size: 14.5px; color: var(--body-gray); line-height: 18px; }

  .contacts { position: absolute; left: 341px; top: 134px; list-style: none; font-size: 14.5px; color: var(--body-gray); line-height: 19px; }
  .contacts li { display: flex; }
  .contact-label { width: 27px; text-align: right; margin-right: 5px; font-weight: 500; color: var(--name-blue); }

  .brand { position: absolute; left: 0; right: 0; top: 97px; text-align: center; }
  .brand-dot { display: block; margin: 0 auto 36px; }
  .brand-name { font-family: "Cinzel", Georgia, serif; font-weight: 500; font-size: 21px; color: var(--silver); line-height: 25px; letter-spacing: 0.5px; }
  .tagline { position: absolute; left: 0; right: 0; top: 281px; text-align: center; font-size: 14.5px; color: var(--white); }
</style>
</head>
<body>
  <section class="card card-front">
    <div class="identity">
      <h1 class="person-name">ELLIS HARROW</h1>
      <p class="person-title">CEO/FOUNDER</p>
      <p class="address">4120 Larkspur Court<br>Juneau, Alaska 34820</p>
    </div>
    <ul class="contacts">
      <li><span class="contact-label">[P]</span>512 904 3376</li>
      <li><span class="contact-label">[C]</span>743 215 6089</li>
      <li><span class="contact-label">[E]</span>care@crestmd.com</li>
      <li><span class="contact-label">[W]</span>www.crestmd.com</li>
    </ul>
  </section>

  <section class="card card-back">
    <div class="brand">
      <svg class="brand-dot" width="70" height="70" viewBox="0 0 70 70" aria-hidden="true">
        <circle cx="35" cy="35" r="34" fill="var(--silver)"/>
      </svg>
      <p class="brand-name">WHITCOMBE MD<br>CREST PRIMARY CARE</p>
    </div>
    <p class="tagline">Where each patient is treated as our only patient</p>
  </section>
</body>
</html>
```